Powerpoint marketing presentation

I wold like to have a powerpoint presentation with includes the attached logo for the company. I would like a background that looks good with the logo. I would like creative slides that capture the contents in an impact way. The Company's name is Veltrane Services and it provides oil and gas well abandonment services. Well abandonments are often the overlooked aspect of a wells lifecycle. This is often overlooked area as it is a non-core activity to the energy company. We ensure this aspect is done in accordance with regulations and in a cost effective way. If possible I would like some creative ideas on a corporate scorecard to report results.

Target Market(s)

Oil and gas exploration and production companies

Industry/Entity Type

It Company

Font styles to use
Sans Serif

Requirements
Must have
• Presentation background incorporating logo. Creative visual capture of the business. This is a sales pitch presentation. It must be impactful.
Nice to have
• I would like to see some scorecard designs.
Should not have
• I am trying to get something that is just words on a page. Design and creativity to communicate.

```html
<!DOCTYPE html>
<html lang="en">
<head>
<meta charset="utf-8">
<title>Veltrane Services – Presentation Deck</title>
<link href="https://fonts.googleapis.com/css2?family=Open+Sans:wght@400;600;700;800&display=swap" rel="stylesheet">
<style>
  :root{
    --page:#e9eaea;
    --green:#3f9a2c;
    --green-dark:#2a7a1e;
    --green-light:#6cbf4f;
    --ink:#2b2b2b;
    --head:#333638;
    --grey:#8d9194;
    --line:#d7d9da;
    --white:#ffffff;
  }
  *{box-sizing:border-box;margin:0;padding:0}
  html,body{width:804px;height:1200px;overflow:hidden}
  body{background:var(--page);font-family:"Open Sans",Arial,sans-serif;color:var(--ink)}
  .deck{display:grid;grid-template-columns:repeat(3,252px);grid-template-rows:repeat(7,155px);gap:14px 12px;padding:14px 12px}
  .slide{position:relative;background:var(--white);overflow:hidden;box-shadow:0 1px 2px rgba(0,0,0,.18)}
  .slide-head{height:16px;background:var(--head);display:flex;align-items:center;color:var(--white);font-size:7.5px;font-weight:700;letter-spacing:.3px;text-transform:uppercase}
  .slide-head::before{content:"";width:16px;height:16px;background:var(--green);margin-right:6px}
  .slide-foot{position:absolute;left:0;right:0;bottom:0;height:9px;background:var(--green);display:flex;align-items:center;padding-left:6px;color:var(--white);font-size:4.5px;font-weight:700;letter-spacing:.3px;text-transform:uppercase}
  .slide-body{position:absolute;top:22px;left:10px;right:10px;bottom:14px}
  .bullets{list-style:none;display:flex;flex-direction:column;gap:7px;margin-top:6px}
  .bullets li{display:flex;align-items:center;gap:6px;font-size:5.5px;color:#555}
  .bullets li::before{content:"";width:7px;height:7px;border-radius:50%;background:var(--green);flex:none}
  .bullets.tight{gap:5px}
  .brand{display:flex;align-items:center;gap:6px;font-weight:800;text-transform:uppercase;letter-spacing:.5px}
  .brand-dot{border-radius:50%;flex:none}
  /* title slides */
  .cover{background:linear-gradient(#f7f7f7,#e4e4e4)}
  .cover .brand{position:absolute;left:16px;top:62px;font-size:12px;color:#b9bcbe}
  .cover .brand-dot{width:26px;height:26px;background:#c9cccd}
  .hero{background:#1e2a2e}
  .hero-photo{position:absolute;inset:0;background:linear-gradient(180deg,#4e6a7a 0%,#2f3d44 60%,#1b2226 100%)}
  .hero-title{position:absolute;left:0;right:0;top:10px;padding:6px 12px;background:rgba(20,28,32,.75);color:var(--white);font-size:10px;font-weight:700;text-align:center;line-height:1.25;text-transform:uppercase}
  .hero-band{position:absolute;left:0;right:0;bottom:0;height:10px;background:var(--green)}
  .logo-slide{display:flex;align-items:center;justify-content:center;gap:10px}
  .logo-slide .brand{font-size:9px;color:var(--green-dark);flex-direction:column;align-items:flex-start;gap:2px}
  .logo-slide .brand-row{display:flex;align-items:center;gap:6px}
  .logo-slide .brand-dot{width:22px;height:22px;background:var(--green)}
  .logo-slide .tag{font-size:6px;color:var(--grey);font-weight:600;border-left:1px solid var(--line);padding-left:8px;max-width:80px;text-transform:uppercase}
  /* panels */
  .panels{display:flex;gap:6px;height:100%}
  .panel{flex:1;background:var(--green);color:var(--white);font-size:6px;font-weight:700;display:flex;flex-direction:column;align-items:center;padding-top:10px;gap:8px;text-transform:uppercase}
  .panel:nth-child(2){background:var(--green-dark)}
  .panel-icon{width:20px;height:20px;border:1.5px solid var(--white);border-radius:50%}
  .panel-lines{width:70%;display:flex;flex-direction:column;gap:3px}
  .panel-lines span{height:2px;background:rgba(255,255,255,.5)}
  /* team table */
  .team{display:flex;flex-direction:column;gap:3px}
  .team-row{display:flex;gap:6px;align-items:center;height:14px}
  .team-role{width:60px;height:100%;background:var(--green);color:var(--white);font-size:5px;font-weight:700;display:flex;align-items:center;justify-content:center;text-transform:uppercase}
  .team-desc{font-size:5px;color:#555}
  .strengths{display:flex;flex-direction:column;gap:10px;margin-top:4px}
  .strength{display:flex;align-items:center;gap:8px;font-size:5.5px;color:#555}
  .strength-badge{width:16px;height:16px;border-radius:50%;background:var(--green);flex:none}
  /* score table */
  .score{width:100%;border-collapse:collapse;font-size:5.5px}
  .score th{background:var(--green);color:var(--white);padding:3px;text-align:left;font-weight:700}
  .score td{padding:3px;border-bottom:1px solid var(--line);color:#555}
  .score td.ok{color:var(--green-dark);font-weight:700}
  /* contact */
  .contact{background:var(--green);color:var(--white)}
  .contact .brand{position:absolute;left:0;right:0;top:28px;justify-content:center;font-size:10px}
  .contact .brand-dot{width:20px;height:20px;background:var(--white)}
  .contact h2{position:absolute;left:0;right:0;top:70px;text-align:center;font-size:17px;font-weight:800}
  .contact p{position:absolute;left:0;right:0;text-align:center;font-size:5.5px}
  svg text{font-family:"Open Sans",Arial,sans-serif}
</style>
</head>
<body>
<main class="deck">

  <section class="slide cover">
    <div class="brand"><span class="brand-dot"></span>Veltrane Services</div>
  </section>

  <section class="slide hero">
    <div class="hero-photo" role="img" aria-label="Oil pumpjack silhouetted against a dusk sky"></div>
    <h1 class="hero-title">Specializing in Inactive Well Management</h1>
    <div class="hero-band"></div>
  </section>

  <section class="slide logo-slide">
    <div class="brand"><div class="brand-row"><span class="brand-dot"></span>Veltrane<br>Services</div></div>
    <div class="tag">Specializing in inactive well management</div>
  </section>

  <section class="slide">
    <header class="slide-head">Overview</header>
    <div class="slide-body">
      <ul class="bullets">
        <li>Inactive well management</li><li>Regulatory compliance support</li><li>Cost effective abandonment</li><li>Site restoration</li>
      </ul>
    </div>
    <footer class="slide-foot">Veltrane Services</footer>
  </section>

  <section class="slide">
    <header class="slide-head">Introduction – Veltrane Services</header>
    <div class="slide-body">
      <ul class="bullets tight">
        <li>Over a decade of field experience</li><li>Focus on non-core well assets</li><li>Trusted by producers across the basin</li><li>Planning through final reclamation</li><li>Lower liability, lower cost</li>
      </ul>
    </div>
    <footer class="slide-foot">Veltrane Services</footer>
  </section>

  <section class="slide">
    <header class="slide-head">Introduction – Veltrane Services</header>
    <div class="slide-body">
      <svg width="232" height="119" viewBox="0 0 232 119">
        <circle cx="116" cy="60" r="36" fill="none" stroke="#6cbf4f" stroke-width="2"/>
        <g fill="#3f9a2c">
          <circle cx="116" cy="22" r="13"/><circle cx="152" cy="48" r="13"/><circle cx="138" cy="92" r="13"/><circle cx="94" cy="92" r="13"/><circle cx="80" cy="48" r="13"/>
        </g>
        <g fill="#555" font-size="5.5" text-anchor="middle">
          <text x="116" y="6">Assess</text><text x="180" y="50">Plan</text><text x="165" y="112">Abandon</text><text x="67" y="112">Reclaim</text><text x="50" y="50">Certify</text>
        </g>
      </svg>
    </div>
    <footer class="slide-foot">Veltrane Services</footer>
  </section>

  <section class="slide">
    <header class="slide-head">Overview</header>
    <div class="slide-body">
      <div class="panels">
        <div class="panel"><span class="panel-icon"></span>Assess<div class="panel-lines"><span></span><span></span><span></span></div></div>
        <div class="panel"><span class="panel-icon"></span>Abandon<div class="panel-lines"><span></span><span></span><span></span></div></div>
        <div class="panel"><span class="panel-icon"></span>Restore<div class="panel-lines"><span></span><span></span><span></span></div></div>
      </div>
    </div>
    <footer class="slide-foot">Veltrane Services</footer>
  </section>

  <section class="slide">
    <header class="slide-head">What we do – Inactive well management</header>
    <div class="slide-body">
      <ul class="bullets tight">
        <li>Well inventory and review</li><li>Liability cost estimates</li><li>Downhole abandonment</li><li>Cut and cap operations</li><li>Surface reclamation</li><li>Regulatory filings</li>
      </ul>
    </div>
    <footer class="slide-foot">Veltrane Services</footer>
  </section>

  <section class="slide">
    <header class="slide-head">Corporate benefits</header>
    <div class="slide-body">
      <ul class="bullets tight">
        <li>Reduced inactive liability</li><li>Predictable program budgets</li><li>Single point of contact</li><li>Full regulatory compliance</li><li>Improved rating with regulator</li><li>More focus on core assets</li>
      </ul>
    </div>
    <footer class="slide-foot">Veltrane Services</footer>
  </section>

  <section class="slide">
    <header class="slide-head">Performance scorecard</header>
    <div class="slide-body">
      <svg width="232" height="119" viewBox="0 0 232 119">
        <g fill="#3f9a2c"><rect x="8" y="58" width="10" height="32"/><rect x="22" y="44" width="10" height="46"/><rect x="36" y="66" width="10" height="24"/></g>
        <line x1="4" y1="90" x2="52" y2="90" stroke="#999" stroke-width=".8"/>
        <g fill="#3f9a2c"><rect x="90" y="70" width="10" height="20"/><rect x="104" y="60" width="10" height="30"/><rect x="118" y="52" width="10" height="38"/></g>
        <line x1="86" y1="90" x2="134" y2="90" stroke="#999" stroke-width=".8"/>
        <text x="192" y="82" font-size="17" font-weight="800" fill="#555" text-anchor="middle">RRB</text>
        <g font-size="5" fill="#555" text-anchor="middle"><text x="28" y="100">Wells abandoned</text><text x="110" y="100">Cost per well</text></g>
      </svg>
    </div>
    <footer class="slide-foot">Veltrane Services</footer>
  </section>

  <section class="slide">
    <header class="slide-head">Summary of risk areas</header>
    <div class="slide-body">
      <svg width="232" height="119" viewBox="0 0 232 119">
        <line x1="20" y1="100" x2="220" y2="100" stroke="#999" stroke-width=".8"/>
        <line x1="20" y1="10" x2="20" y2="100" stroke="#999" stroke-width=".8"/>
        <rect x="52" y="80" width="22" height="20" fill="#8d9194"/>
        <rect x="100" y="18" width="22" height="82" fill="#3f9a2c"/>
        <rect x="148" y="66" width="22" height="34" fill="#3f9a2c"/>
        <rect x="176" y="90" width="10" height="10" fill="#333638"/>
      </svg>
    </div>
    <footer class="slide-foot">Veltrane Services</footer>
  </section>

  <section class="slide">
    <header class="slide-head">Summary of risk areas</header>
    <div class="slide-body">
      <svg width="232" height="119" viewBox="0 0 232 119">
        <line x1="40" y1="4" x2="40" y2="104" stroke="#999" stroke-width=".8"/>
        <g fill="#3f9a2c">
          <rect x="40" y="10" width="170" height="7"/><rect x="40" y="24" width="120" height="7"/><rect x="40" y="38" width="90" height="7"/>
          <rect x="40" y="52" width="60" height="7"/><rect x="40" y="66" width="42" height="7"/><rect x="40" y="80" width="28" height="7"/><rect x="40" y="94" width="16" height="7"/>
        </g>
      </svg>
    </div>
    <footer class="slide-foot">Veltrane Services</footer>
  </section>

  <section class="slide">
    <header class="slide-head">Summary of inactive wells by area</header>
    <div class="slide-body">
      <svg width="232" height="119" viewBox="0 0 232 119">
        <g font-size="5" fill="#555" text-anchor="end"><text x="34" y="16">North</text><text x="34" y="34">Central</text><text x="34" y="52">South</text><text x="34" y="70">East</text><text x="34" y="88">West</text></g>
        <line x1="38" y1="4" x2="38" y2="96" stroke="#999" stroke-width=".8"/>
        <rect x="38" y="10" width="70" height="8" fill="#3f9a2c"/><rect x="108" y="10" width="40" height="8" fill="#8d9194"/>
        <rect x="38" y="28" width="50" height="8" fill="#3f9a2c"/>
        <rect x="38" y="46" width="30" height="8" fill="#3f9a2c"/>
        <rect x="38" y="64" width="20" height="8" fill="#3f9a2c"/>
        <rect x="38" y="82" width="12" height="8" fill="#3f9a2c"/>
      </svg>
    </div>
    <footer class="slide-foot">Veltrane Services</footer>
  </section>

  <section class="slide">
    <header class="slide-head">The team</header>
    <div class="slide-body">
      <div class="team">
        <div class="team-row"><span class="team-role">Director</span><span class="team-desc">Strategy and client relations</span></div>
        <div class="team-row"><span class="team-role">Operations</span><span class="team-desc">Program execution</span></div>
        <div class="team-row"><span class="team-role">Engineering</span><span class="team-desc">Well design and review</span></div>
        <div class="team-row"><span class="team-role">Regulatory</span><span class="team-desc">Filings and approvals</span></div>
        <div class="team-row"><span class="team-role">Field</span><span class="team-desc">Rig and crew supervision</span></div>
        <div class="team-row"><span class="team-role">Finance</span><span class="team-desc">Budgets and reporting</span></div>
      </div>
    </div>
    <footer class="slide-foot">Veltrane Services</footer>
  </section>

  <section class="slide">
    <header class="slide-head">The team – Key strengths</header>
    <div class="slide-body">
      <div class="strengths">
        <div class="strength"><span class="strength-badge"></span>Proven record of safe abandonment programs</div>
        <div class="strength"><span class="strength-badge"></span>Strong working ties with regulators</div>
        <div class="strength"><span class="strength-badge"></span>Flexible crews for any program size</div>
      </div>
    </div>
    <footer class="slide-foot">Veltrane Services</footer>
  </section>

  <section class="slide">
    <header class="slide-head">Abandon vs Suspend</header>
    <div class="slide-body">
      <ul class="bullets">
        <li>Suspend: defers cost, keeps liability</li><li>Abandon: closes liability for good</li><li>Rising fees for inactive wells</li><li>Plan the right path per well</li>
      </ul>
    </div>
    <footer class="slide-foot">Veltrane Services</footer>
  </section>

  <section class="slide">
    <header class="slide-head">Scorecard to report results</header>
    <div class="slide-body">
      <table class="score">
        <thead><tr><th>Metric</th><th>Target</th><th>Actual</th></tr></thead>
        <tbody>
          <tr><td>Wells abandoned</td><td>40</td><td class="ok">38</td></tr>
          <tr><td>Sites reclaimed</td><td>25</td><td class="ok">27</td></tr>
          <tr><td>Cost per well</td><td>$90k</td><td class="ok">$84k</td></tr>
          <tr><td>Safety incidents</td><td>0</td><td class="ok">0</td></tr>
        </tbody>
      </table>
    </div>
    <footer class="slide-foot">Veltrane Services</footer>
  </section>

  <section class="slide contact">
    <div class="brand"><span class="brand-dot"></span>Veltrane Services</div>
    <h2>CONTACT US...</h2>
    <p style="top:100px">555-010-2040</p>
    <p style="top:110px">info@veltrane.example</p>
  </section>

</main>
</body>
</html>
```